Flyer for the Harvest Lantern Gathering 2018

Design a flyer for our annual conference with basic information about the conference: conference logo and year,

Location:
Dunmore Community Center (Downtown Portland)
482 Willowby Street, Portland, ME 04117,

Date:
August 24th, 25th and 26th, 2018
Start time 6:00PM

I would like the following three words added to the flyer. These words describe the vision of the conference:
Prophetic, Worship, Prayer

```html
<!DOCTYPE html>
<html lang="en">
<head>
<meta charset="utf-8">
<title>Harvest Lantern Gathering 2018 Flyer</title>
<link href="https://fonts.googleapis.com/css2?family=Orbitron:wght@700;800&family=Roboto:wght@400;500;700&display=swap" rel="stylesheet">
<style>
  :root {
    --backdrop: #b3b0ad;
    --flyer-dark: #121212;
    --flyer-mid: #262626;
    --accent: #f0a20c;
    --gold: #e5b320;
    --white: #ffffff;
    --text-soft: #f2f2f2;
  }
  * { margin: 0; padding: 0; box-sizing: border-box; }
  html, body {
    width: 1122px; height: 1200px; overflow: hidden;
    background: var(--backdrop);
  }
  .flyer {
    position: absolute; left: 157px; top: 30px;
    width: 807px; height: 1140px; overflow: hidden;
    background: radial-gradient(ellipse at 50% 62%, var(--flyer-mid) 0%, var(--flyer-dark) 70%);
    font-family: "Roboto", Arial, sans-serif;
  }
  .hero { position: absolute; left: 0; top: 0; width: 807px; height: 540px; }
  .title {
    position: absolute; left: 0; width: 100%; top: 572px; text-align: center;
    font-family: "Orbitron", "Arial Black", sans-serif; font-weight: 800;
    font-size: 64px; letter-spacing: 2px; color: var(--accent); line-height: 1;
  }
  .subtitle {
    position: absolute; left: 0; width: 100%; top: 650px; text-align: center;
    font-weight: 700; font-size: 42px; color: var(--white); line-height: 1;
  }
  .brand-mark {
    position: absolute; left: 335px; top: 726px; width: 138px; height: 138px;
    border-radius: 50%; border: 4px solid var(--gold);
  }
  .brand-name {
    position: absolute; left: 0; width: 100%; top: 870px; text-align: center;
    font-weight: 700; font-size: 38px; letter-spacing: 3px; color: var(--white); line-height: 1;
  }
  .vision {
    position: absolute; left: 129px; top: 938px; display: flex; align-items: center;
    font-weight: 500; font-size: 30px; color: var(--accent); line-height: 1;
  }
  .vision .divider { width: 2px; height: 32px; background: var(--text-soft); margin: 0 30px; }
  .info { position: absolute; top: 1028px; }
  .info-location { left: 31px; width: 384px; }
  .info-date { left: 492px; width: 277px; }
  .info-head { display: flex; align-items: center; }
  .info-head svg { width: 22px; height: 22px; margin-right: 8px; flex: none; }
  .info-label { font-weight: 500; font-size: 18px; color: var(--accent); letter-spacing: 0.5px; }
  .info-rule { flex: 1; height: 2px; background: var(--accent); margin-left: 8px; }
  .info-body {
    margin-left: 30px; margin-top: 10px;
    font-size: 16px; line-height: 21px; color: var(--text-soft);
  }
</style>
</head>
<body>
  <main class="flyer">
    <svg class="hero" viewBox="0 0 807 540" aria-hidden="false">
      <defs>
        <radialGradient id="hero-glow" cx="0.5" cy="0.55" r="0.7">
          <stop offset="0" stop-color="#fff4e6"/>
          <stop offset="0.25" stop-color="#ffc27a"/>
          <stop offset="0.55" stop-color="#f1772c"/>
          <stop offset="0.85" stop-color="#d44a2a"/>
          <stop offset="1" stop-color="#b5379a"/>
        </radialGradient>
        <linearGradient id="hero-shade" x1="0" y1="0" x2="0" y2="1">
          <stop offset="0.55" stop-color="#3a1e14" stop-opacity="0"/>
          <stop offset="1" stop-color="#2a1712" stop-opacity="0.75"/>
        </linearGradient>
        <linearGradient id="rim" x1="0" y1="0" x2="1" y2="0">
          <stop offset="0" stop-color="#b8860b"/>
          <stop offset="0.5" stop-color="#f5c629"/>
          <stop offset="1" stop-color="#b8860b"/>
        </linearGradient>
      </defs>
      <g role="img" aria-label="Photo of a worship crowd facing a glowing stage cross under a sunset sky">
        <path d="M0,0 H807 V280 Q403,770 0,318 Z" fill="url(#hero-glow)"/>
        <path d="M0,0 H807 V280 Q403,770 0,318 Z" fill="url(#hero-shade)"/>
      </g>
      <path d="M0,318 Q403,770 807,280" fill="none" stroke="url(#rim)" stroke-width="6"/>
    </svg>

    <h1 class="title">HLGCON 2018</h1>
    <p class="subtitle">Harvest Lantern Gathering</p>

    <div class="brand-mark"></div>
    <p class="brand-name">HLGCON</p>

    <div class="vision">
      <span>PROPHETIC</span><span class="divider"></span>
      <span>WORSHIP</span><span class="divider"></span>
      <span>PRAYER</span>
    </div>

    <section class="info info-location">
      <div class="info-head">
        <svg viewBox="0 0 24 24"><path d="M12 2a7 7 0 0 0-7 7c0 5 7 13 7 13s7-8 7-13a7 7 0 0 0-7-7zm0 9.5A2.5 2.5 0 1 1 12 6.5a2.5 2.5 0 0 1 0 5z" fill="#ffffff"/></svg>
        <span class="info-label">LOCATION:</span><span class="info-rule"></span>
      </div>
      <p class="info-body">Dunmore Community Center (Downtown Portland)<br>482 Willowby Street, Portland, ME 04117,</p>
    </section>

    <section class="info info-date">
      <div class="info-head">
        <svg viewBox="0 0 24 24"><rect x="3" y="5" width="18" height="16" rx="2" fill="#ffffff"/><rect x="7" y="2" width="2" height="5" fill="#ffffff"/><rect x="15" y="2" width="2" height="5" fill="#ffffff"/><rect x="5" y="9" width="14" height="10" fill="#121212"/><g fill="#ffffff"><rect x="6.5" y="10.5" width="3" height="3"/><rect x="10.5" y="10.5" width="3" height="3"/><rect x="14.5" y="10.5" width="3" height="3"/><rect x="6.5" y="14.5" width="3" height="3"/><rect x="10.5" y="14.5" width="3" height="3"/><rect x="14.5" y="14.5" width="3" height="3"/></g></svg>
        <span class="info-label">DATE:</span><span class="info-rule"></span>
      </div>
      <p class="info-body">August 24th, 25th and 26th, 2018<br>Start time 6:00PM</p>
    </section>
  </main>
</body>
</html>
```